20/20 Referral Program for Optometry (Eye Doctor) Office

Hello - We looking for a flyer with a card that can be torn off at the bottom for our referral program. The flyer needs to be simple and can basically be business card on top of another with the following information. Look at the files I made a sketch of what I have in mind. We do need images that will fill in the space

Basically we are giving $20 to a person if they refer someone and then that person will receive $20 towards eyewear or an annual supply of contact lenses
http://harborlineoptics.com/2020-referral-program/

The card should have name and email of who referred them along with text that states that they will receive $20 towards the purchase of eyewear or contact lenses

http://harborlineoptics.com/wp-content/uploads/2015/02/20.20-Website-Referral-Cards.pdf

Branding look at the following files and on our website www.willowbrightvision.com

Target Market(s)

Current patients... this will be given to patients after an eye exam and they can give to a friend or family member

Industry/Entity Type

Doctor

Font styles to use
Serif
Sans Serif

Requirements
Must have
• Logo... definition of the program and a card for people to give out to friends and family. Please note this is for Willowbright Vision so use that logo. Also the barn or mountain of larkspur ski resort is nice
• Also do not use the text on Broken Glasses flyer that was for a different audience. Text can be found at the following address
• http://harborlineoptics.com/2020-referral-program/
Nice to have
• Clean look and feel. We do not need it to be text heavy we can refer to the website for Terms and Conditions
Should not have
• Up to you be creative

```html
<!DOCTYPE html>
<html lang="en">
<head>
<meta charset="utf-8">
<title>Willowbright Vision – 20/20 Referral Card</title>
<link rel="stylesheet" href="https://fonts.googleapis.com/css2?family=Open+Sans:wght@400;600;700&display=swap">
<style>
  :root {
    --page-bg: #3a3a3a;
    --card-bg: #f7f7f6;
    --brand-red: #8e1b1f;
    --ink: #2e2e2e;
    --rule: #d9d9d9;
    --badge-blue: #bfe0f2;
    --badge-ring: #7fbcdc;
  }
  * { box-sizing: border-box; margin: 0; padding: 0; }
  html, body { width: 1200px; height: 900px; overflow: hidden; }
  body {
    background: var(--page-bg);
    font-family: "Open Sans", Arial, sans-serif;
    position: relative;
  }
  .card {
    position: absolute;
    top: 300px;
    width: 520px;
    height: 300px;
    background: var(--card-bg);
    border-radius: 22px;
    overflow: hidden;
  }
  .card--front { left: 60px; }
  .card--back { left: 620px; }

  /* front */
  .brand {
    position: absolute;
    left: 0; top: 0;
    width: 250px; height: 300px;
    display: flex; flex-direction: column; align-items: center; justify-content: center;
    gap: 28px;
  }
  .brand__name {
    color: var(--brand-red);
    font-weight: 700;
    font-size: 26px;
    line-height: 1;
    text-align: center;
  }
  .brand__badge {
    width: 76px; height: 76px;
    border-radius: 50%;
    background: var(--badge-blue);
    border: 3px solid var(--badge-ring);
  }
  .divider {
    position: absolute;
    left: 250px; top: 28px;
    width: 1px; height: 200px;
    background: var(--rule);
  }
  .details {
    position: absolute;
    left: 272px; top: 40px;
    right: 20px;
  }
  .doctors {
    color: var(--brand-red);
    font-weight: 600;
    font-size: 19px;
    line-height: 1.2;
  }
  .program { margin-top: 24px; font-size: 15px; line-height: 1.4; }
  .program__number { color: var(--brand-red); font-weight: 600; }
  .program__title { color: var(--ink); font-weight: 700; }
  .contact { margin-top: 20px; list-style: none; font-size: 15px; color: var(--ink); }
  .contact li { display: flex; align-items: center; gap: 10px; line-height: 1.7; }
  .contact svg { width: 13px; height: 13px; fill: var(--brand-red); flex: none; }

  /* back */
  .offer {
    position: absolute;
    left: 34px; top: 32px; right: 30px;
    color: var(--brand-red);
    font-weight: 600;
    font-size: 15px;
    line-height: 1.35;
  }
  .form { position: absolute; left: 54px; top: 92px; right: 60px; list-style: none; }
  .form li {
    display: flex; align-items: flex-end; gap: 8px;
    color: var(--brand-red); font-weight: 600; font-size: 15px;
    height: 34px;
  }
  .form .fill { flex: 1; border-bottom: 2px dotted var(--ink); margin-bottom: 5px; }
  .sign-off {
    position: absolute; left: 54px; top: 214px;
    color: var(--brand-red); font-weight: 600; font-size: 16px;
  }
  .base-rule {
    position: absolute; left: 70px; right: 24px; bottom: 26px;
    height: 2px; background: var(--brand-red);
  }
  .flourish {
    position: absolute;
    background: linear-gradient(90deg, rgba(142,27,31,0.15), rgba(142,27,31,0.45));
    border-radius: 4px;
  }
  .flourish--right { right: 24px; bottom: 30px; width: 90px; height: 26px; }
  .flourish--left { left: 14px; bottom: 14px; width: 56px; height: 24px; }
</style>
</head>
<body>
  <section class="card card--front" aria-label="Referral card front">
    <div class="brand">
      <div class="brand__name">Willowbright Vision</div>
      <div class="brand__badge" aria-hidden="true"></div>
    </div>
    <div class="divider"></div>
    <div class="details">
      <p class="doctors">Dr. Nadia Ellsworth<br>Dr. Owen Hartley</p>
      <p class="program"><span class="program__number">20/20</span><br><span class="program__title">Referral Program</span></p>
      <ul class="contact">
        <li>
          <svg viewBox="0 0 24 24" aria-hidden="true"><path d="M6.6 10.8a15.1 15.1 0 0 0 6.6 6.6l2.2-2.2c.3-.3.7-.4 1-.2 1.1.4 2.3.6 3.6.6.6 0 1 .4 1 1V20c0 .6-.4 1-1 1A17 17 0 0 1 3 4c0-.6.4-1 1-1h3.5c.6 0 1 .4 1 1 0 1.3.2 2.5.6 3.6.1.3 0 .7-.2 1z"/></svg>
          <span>970-555-0142</span>
        </li>
        <li>
          <svg viewBox="0 0 24 24" aria-hidden="true"><circle cx="12" cy="12" r="11"/></svg>
          <span>www.willowbrightvision.com</span>
        </li>
      </ul>
    </div>
  </section>

  <section class="card card--back" aria-label="Referral card back">
    <p class="offer">Present this card at your first appointment for $20<br>towards eye wear or contact lenses</p>
    <ul class="form">
      <li><span>Referred by:</span><span class="fill"></span></li>
      <li><span>Name :</span><span class="fill"></span></li>
      <li><span>Email :</span><span class="fill"></span></li>
    </ul>
    <p class="sign-off">We can't wait to SEE you!</p>
    <div class="base-rule" aria-hidden="true"></div>
    <div class="flourish flourish--right" role="img" aria-label="Scrolling ornament in brand red"></div>
    <div class="flourish flourish--left" role="img" aria-label="Scrolling ornament in brand red"></div>
  </section>
</body>
</html>
```